Design a stunning business card

Needed a trendy business card. Here are the details for the front and back. The logo is also attached. I will award the contest as soon as I find a cool design. Thanks for your interest in the contest and your creativity!

FRONT:
LM Craft Works
-Remodeling, Remediation and Restoration
-General contractors
-Licensed, Bonded and Insured

Mobile: 202-555-0147
Fax: 202-555-0183
Toll-free: 1-833-555-0162
Email: Service@lmCraftWorks.example
4870 R ST NW, #210, Washington, DC 20007
***Suggested for front is company logo attached

BACK:
We are hiring! Estamos contratando!
Master Carpenters, Drywall Installers, Construction Foreman
Call: 202-555-0147

***Suggested for back are logos of NestFinder , BVQ Certified Firm and Watt Badge

```html
<!DOCTYPE html>
<html lang="en">
<head>
<meta charset="utf-8">
<title>LM Craft Works – Business Card</title>
<link rel="stylesheet" href="https://fonts.googleapis.com/css2?family=Lato:wght@400;700;900&display=swap">
<style>
  :root{
    --stage:#e9ebee;
    --brand:#2e9cc8;
    --brand-dark:#1c7aa3;
    --ink:#2f3a44;
    --paper:#ffffff;
    --badge-grey:#8a9198;
    --badge-green:#5fae3e;
  }
  *{box-sizing:border-box;margin:0;padding:0}
  html,body{width:1200px;height:773px;overflow:hidden}
  body{
    background:var(--stage);
    font-family:"Lato",sans-serif;
    display:flex;align-items:center;justify-content:center;gap:48px;
  }
  .card{position:relative;overflow:hidden;box-shadow:0 8px 24px rgba(0,0,0,.18)}

  /* FRONT (portrait) */
  .card-front{width:300px;height:480px;background:var(--paper);border:4px solid var(--brand)}
  .front-band{position:absolute;inset:0;width:100%;height:100%}
  .brand-block{position:absolute;left:26px;right:20px;top:36px}
  .brand-mark{display:flex;align-items:center;gap:10px}
  .brand-mark .dot{width:34px;height:34px;border-radius:50%;background:var(--brand);flex:none}
  .brand-mark .name{font-size:22px;font-weight:700;color:var(--brand);line-height:1.1}
  .services{list-style:none;margin-top:24px;font-size:12px;color:var(--ink);line-height:1.55}
  .services li{display:flex;gap:7px;align-items:flex-start}
  .services li::before{
    content:"";flex:none;margin-top:5px;width:0;height:0;
    border-left:6px solid var(--brand);border-top:4px solid transparent;border-bottom:4px solid transparent;
  }
  .identity{position:absolute;left:24px;right:16px;top:272px;color:var(--paper)}
  .identity .person{font-size:22px;font-weight:700;letter-spacing:.3px}
  .identity .role{font-size:11.5px;margin-top:1px;opacity:.9}
  .contact-list{list-style:none;margin-top:12px;font-size:11.5px;line-height:1.7}
  .contact-list li{display:flex;align-items:center;gap:8px;white-space:nowrap}
  .contact-list svg{width:11px;height:11px;flex:none;fill:var(--paper)}
  .address{position:absolute;left:24px;right:12px;bottom:18px;color:var(--paper);font-size:11px;white-space:nowrap}

  /* BACK (landscape) */
  .card-back{width:520px;height:300px;background:var(--brand);display:flex;align-items:center;justify-content:center}
  .back-frame{position:absolute;inset:10px;border:2px solid var(--paper)}
  .back-content{position:relative;text-align:center;color:var(--paper);width:100%}
  .hiring{font-size:19px;font-weight:900}
  .roles{display:flex;justify-content:center;gap:14px;margin-top:6px;font-size:11.5px}
  .roles span::before{content:"\2713";margin-right:4px}
  .call{font-size:30px;font-weight:900;margin-top:14px;letter-spacing:.5px}
  .badges{display:flex;justify-content:center;align-items:center;gap:22px;margin-top:14px}
  .badge{border-radius:50%;background:var(--paper)}
  .badge-a{width:50px;height:50px;border-radius:6px;background:var(--brand-dark);border:2px solid var(--paper)}
  .badge-b{width:46px;height:46px;border:6px solid var(--badge-green)}
  .badge-c{width:50px;height:50px;border:6px solid var(--badge-grey)}
  .division{font-size:11px;font-weight:700;margin-top:16px}
</style>
</head>
<body>

  <section class="card card-front" aria-label="Business card front">
    <svg class="front-band" viewBox="0 0 292 472" preserveAspectRatio="none" aria-hidden="true">
      <path d="M0 472 V258 C90 252 200 240 292 206 V472 Z" fill="var(--brand)"/>
    </svg>
    <div class="brand-block">
      <div class="brand-mark"><span class="dot"></span><span class="name">LM Craft Works</span></div>
      <ul class="services">
        <li>Remodeling, Remediation and Restoration</li>
        <li>General contractors</li>
        <li>Licensed, Bonded and Insured</li>
      </ul>
    </div>
    <div class="identity">
      <div class="person">Daniel Reyes</div>
      <div class="role">CEO</div>
      <ul class="contact-list">
        <li><svg viewBox="0 0 24 24"><path d="M6.6 10.8a15 15 0 006.6 6.6l2.2-2.2a1 1 0 011-.25 11 11 0 003.5.56 1 1 0 011 1V20a1 1 0 01-1 1A17 17 0 013 4a1 1 0 011-1h3.5a1 1 0 011 1 11 11 0 00.56 3.5 1 1 0 01-.25 1z"/></svg>202-555-0147</li>
        <li><svg viewBox="0 0 24 24"><path d="M6 2h9l3 3v5H6zM4 11h16a2 2 0 012 2v7H2v-7a2 2 0 012-2z"/></svg>202-555-0183</li>
        <li><svg viewBox="0 0 24 24"><path d="M6.6 10.8a15 15 0 006.6 6.6l2.2-2.2a1 1 0 011-.25 11 11 0 003.5.56 1 1 0 011 1V20a1 1 0 01-1 1A17 17 0 013 4a1 1 0 011-1h3.5a1 1 0 011 1 11 11 0 00.56 3.5 1 1 0 01-.25 1z"/></svg>1-833-555-0162 (Toll Free)</li>
        <li><svg viewBox="0 0 24 24"><path d="M2 5h20v14H2zM2 5l10 8 10-8" stroke="#1c7aa3" stroke-width="1.5"/></svg>Service@lmCraftWorks.example</li>
      </ul>
    </div>
    <div class="address">4870 R ST NW, #210, Washington, DC 20007</div>
  </section>

  <section class="card card-back" aria-label="Business card back">
    <div class="back-frame"></div>
    <div class="back-content">
      <div class="hiring">We are hiring! Estamos contratando!</div>
      <div class="roles"><span>Master Carpenters</span><span>Drywall Installers</span><span>Construction Foreman</span></div>
      <div class="call">Call: 202-555-0147</div>
      <div class="badges">
        <div class="badge badge-a" role="img" aria-label="Watt Badge partner badge"></div>
        <div class="badge badge-b" role="img" aria-label="BVQ Certified Firm badge"></div>
        <div class="badge badge-c" role="img" aria-label="NestFinder listing badge"></div>
      </div>
      <p class="division">“ LM Craft Works is a division of Harbor Row Partners LLC ”</p>
    </div>
  </section>

</body>
</html>
```